Facebook Design Project

We need a facebook design for my new edgy consulting business specializing in innovation, technology and strategy.

It is our personal goal to turn each client into raving fans by helping them achieve their own business goals and aspirations through assisting them in raising their own innovation and marketing standards.

We provide our personalised and state-of-the-art services to our clients and boards who represent some of the world greatest innovative thinkers.

Target Market(s)

Executives, Digital Directors, CFO, CEOs and Small Business

Industry/Entity Type

Marketing

Requirements
Must have
• Must Have:
- Please use some of the personal image(s) contained in the zip files which can be downloaded from here

http://vorbex.io/7K9P4T218M5D
http://vorbex.io/8f6r493H1k77
http://vorbex.io/5H8X6W4J9T3m

Nice to have
• Personable design

```html
<!DOCTYPE html>
<html lang="en">
<head>
<meta charset="utf-8">
<title>Daniel Ashcombe Consultancy – Cover Design</title>
<link rel="stylesheet" href="https://fonts.googleapis.com/css2?family=Anton&family=Oswald:wght@300&display=swap">
<style>
  :root {
    --backdrop: #4b4b4b;
    --cover-bg: #ffffff;
    --frame-line: #1a1a1a;
    --title-blue: #0e3c7c;
    --arrow-light: #f7a532;
    --arrow-dark: #e97800;
    --silver-text: #cfcfcf;
    --silver-shade: #9a9a9a;
    --silver-faint: rgba(190, 190, 190, 0.45);
    --suit-dark: #1d1f24;
    --shirt-light: #eef0f3;
    --skin-tone: #d9a98c;
  }
  * { margin: 0; padding: 0; box-sizing: border-box; }
  html, body {
    width: 1200px;
    height: 848px;
    overflow: hidden;
    background: var(--backdrop);
  }
  .stage {
    position: absolute;
    left: 55px;
    top: 195px;
    width: 947px;
    height: 398px;
    transform: scale(1.15);
    transform-origin: top left;
  }
  .cover {
    position: absolute;
    left: 0;
    top: 0;
    width: 947px;
    height: 352px;
    background: var(--cover-bg);
    border: 1px solid var(--frame-line);
    overflow: hidden;
  }
  .growth-arrow {
    position: absolute;
    left: 82px;
    top: 106px;
    width: 167px;
    height: 246px;
    background: linear-gradient(180deg, var(--arrow-light) 0%, var(--arrow-dark) 100%);
  }
  .success-word,
  .success-reflection {
    position: absolute;
    left: 24px;
    width: 270px;
    font-family: "Anton", sans-serif;
    font-weight: 400;
    font-size: 86px;
    line-height: 86px;
    letter-spacing: 1px;
    text-align: center;
  }
  .success-word {
    top: 8px;
    color: var(--silver-text);
    text-shadow: 3px 3px 0 var(--silver-shade);
  }
  .success-reflection {
    top: 82px;
    color: var(--silver-faint);
    transform: scaleY(-1);
    -webkit-mask-image: linear-gradient(0deg, #000 0%, transparent 80%);
    mask-image: linear-gradient(0deg, #000 0%, transparent 80%);
  }
  .brand-title {
    position: absolute;
    right: 323px;
    top: 50px;
    font-family: "Oswald", sans-serif;
    font-weight: 300;
    font-variant: small-caps;
    font-size: 53px;
    line-height: 65px;
    letter-spacing: 1px;
    color: var(--title-blue);
    text-align: right;
    white-space: nowrap;
  }
  .brand-title span { display: block; }
  .portrait-main {
    position: absolute;
    left: 724px;
    top: 41px;
    width: 223px;
    height: 311px;
    background: linear-gradient(180deg, var(--cover-bg) 0%, var(--skin-tone) 14%, var(--skin-tone) 30%, var(--shirt-light) 34%, var(--suit-dark) 48%, var(--suit-dark) 100%);
    border-radius: 90px 90px 0 0;
  }
  .profile-frame {
    position: absolute;
    left: 26px;
    top: 247px;
    width: 151px;
    height: 152px;
    background: var(--cover-bg);
    border: 1px solid var(--frame-line);
    overflow: hidden;
  }
  .portrait-profile {
    position: absolute;
    left: 20px;
    top: 6px;
    width: 100px;
    height: 146px;
    background: linear-gradient(180deg, var(--cover-bg) 0%, var(--skin-tone) 10%, var(--skin-tone) 30%, var(--shirt-light) 34%, var(--suit-dark) 44%, var(--suit-dark) 100%);
    border-radius: 40px 40px 0 0;
  }
</style>
</head>
<body>
  <main class="stage">
    <section class="cover">
      <div class="growth-arrow" role="img" aria-label="Orange upward arrow illustration rising towards the word success"></div>
      <p class="success-word">SUCCESS</p>
      <p class="success-reflection" aria-hidden="true">SUCCESS</p>
      <h1 class="brand-title">
        <span>Daniel Ashcombe</span>
        <span>Consultancy</span>
      </h1>
      <div class="portrait-main" role="img" aria-label="Portrait photo of the consultant in a dark suit and blue tie"></div>
    </section>
    <div class="profile-frame">
      <div class="portrait-profile" role="img" aria-label="Full-length profile photo of the consultant in a dark suit"></div>
    </div>
  </main>
</body>
</html>
```